Redesign of dating app main page

Task is redesign of main page of dating app. Page design is attached. UX design should be the same (buttons of the top of screen , scrolling down). Searching users profiles with their buttons should be more divided.

```html
<!DOCTYPE html>
<html lang="en">
<head>
<meta charset="UTF-8">
<title>Dating App – Main Page</title>
<link href="https://fonts.googleapis.com/css2?family=Open+Sans:wght@400;500;600&display=swap" rel="stylesheet">
<style>
  :root {
    --page-bg: #ffffff;
    --icon-grey: #8c8c8c;
    --divider: #a6a6a6;
    --soft-divider: #dedede;
    --card-border: #dcdcdc;
    --card-bg: #ffffff;
    --list-bg: #f2f2f2;
    --action-bg: #fafafa;
    --text-dark: #333333;
    --text-muted: #8a8a8a;
    --like-green: #6ccf7f;
    --pass-red: #c0392b;
    --dot-inactive: #ffffff;
  }
  * { margin: 0; padding: 0; box-sizing: border-box; }
  html, body {
    width: 1200px;
    height: 2598px;
    overflow: hidden;
    background: var(--page-bg);
    font-family: "Open Sans", Arial, sans-serif;
    color: var(--text-dark);
  }
  .screen { position: relative; width: 1200px; height: 2598px; }

  /* Top navigation */
  .top-nav { position: absolute; left: 0; top: 0; width: 1200px; height: 214px; border-bottom: 3px solid var(--divider); }
  .nav-icon { position: absolute; top: 80px; width: 96px; height: 96px; }
  .nav-icon svg { width: 100%; height: 100%; display: block; }
  .nav-profile { left: 48px; }
  .nav-matches { left: 554px; }
  .nav-messages { left: 1050px; }

  /* Featured profile card */
  .featured-card {
    position: absolute; left: 112px; top: 300px; width: 998px; height: 1290px;
    background: var(--card-bg); border: 3px solid var(--card-border); border-radius: 12px;
    box-shadow: 0 4px 12px rgba(0,0,0,0.08); overflow: hidden;
  }
  .featured-header { position: absolute; left: 45px; right: 38px; top: 36px; height: 64px; display: flex; align-items: center; }
  .featured-name { font-size: 54px; font-weight: 500; letter-spacing: 1px; margin-right: 38px; }
  .featured-age { font-size: 52px; color: var(--text-muted); margin-right: 38px; }
  .featured-job { font-size: 44px; color: var(--text-muted); }
  .distance { display: flex; align-items: center; gap: 10px; font-size: 38px; color: var(--text-muted); white-space: nowrap; }
  .featured-header .distance { margin-left: auto; }
  .distance svg { width: 32px; height: 44px; }

  .featured-photo {
    position: absolute; left: 32px; top: 115px; width: 928px; height: 957px;
    background: radial-gradient(ellipse at 50% 55%, #d9c3b5 0%, #a89a93 28%, #5f6063 55%, #9a9c9f 80%, #c9cacc 100%);
  }
  .photo-dots { position: absolute; left: 298px; bottom: 32px; display: flex; gap: 51px; }
  .photo-dot { width: 26px; height: 26px; border-radius: 50%; background: var(--dot-inactive); }
  .photo-dot.is-active { background: var(--like-green); }

  .featured-actions {
    position: absolute; left: 0; right: 0; top: 1104px; bottom: 0;
    background: var(--action-bg); border-top: 3px solid var(--soft-divider);
  }
  .action-pass { position: absolute; left: 79px; top: 40px; width: 104px; height: 104px; }
  .action-like { position: absolute; right: 79px; top: 40px; width: 104px; height: 104px; }
  .action-pass svg, .action-like svg { width: 100%; height: 100%; display: block; }
  .see-more { position: absolute; left: 0; right: 0; top: 70px; text-align: center; font-size: 32px; font-weight: 500; letter-spacing: 1px; color: var(--text-dark); }

  /* Profile list */
  .profile-row {
    position: absolute; left: 112px; width: 998px; height: 314px;
    background: var(--list-bg); border-radius: 12px; box-shadow: 0 4px 10px rgba(0,0,0,0.18); overflow: hidden;
  }
  .profile-row.row-one { top: 1660px; }
  .profile-row.row-two { top: 2044px; }
  .row-photo { position: absolute; left: 0; top: 0; width: 266px; height: 314px; }
  .row-one .row-photo { background: linear-gradient(160deg, #e0a06e 0%, #b8653a 45%, #6e3a22 100%); }
  .row-two .row-photo { background: linear-gradient(160deg, #5a7a3c 0%, #2f3d24 50%, #1c1d1a 100%); }
  .row-name { position: absolute; left: 310px; top: 52px; font-size: 50px; font-weight: 500; letter-spacing: 1px; }
  .row-age { position: absolute; left: 310px; top: 130px; font-size: 48px; color: var(--text-muted); }
  .row-job { position: absolute; left: 310px; top: 198px; font-size: 44px; color: var(--text-muted); }
  .row-distance { position: absolute; right: 190px; top: 214px; }

  .row-actions {
    position: absolute; right: 0; top: 0; width: 150px; height: 314px;
    background: var(--action-bg); border-left: 3px solid var(--soft-divider);
  }
  .mini-pass, .mini-like { position: absolute; left: 37px; width: 76px; height: 76px; }
  .mini-pass { top: 60px; }
  .mini-like { top: 178px; }
  .mini-pass svg, .mini-like svg { width: 100%; height: 100%; display: block; }
</style>
</head>
<body>
<div class="screen">

  <header class="top-nav">
    <div class="nav-icon nav-profile" aria-label="Profile">
      <svg viewBox="0 0 30 30"><circle cx="15" cy="9" r="7" fill="var(--icon-grey)"/><path d="M1 29 C1 20 8 17 15 17 C22 17 29 20 29 29 Z" fill="var(--icon-grey)"/></svg>
    </div>
    <div class="nav-icon nav-matches" aria-label="Matches">
      <svg viewBox="0 0 30 30"><path d="M15 1 C23 1 29 6.5 29 13.5 C29 20.5 23 26 15 26 L9 29 L10 24 C4.5 22 1 18 1 13.5 C1 6.5 7 1 15 1 Z" fill="var(--icon-grey)"/><path d="M15 20 L8.5 13.5 C6.5 11.5 7.5 8 10.5 8 C12.5 8 14 9.5 15 11 C16 9.5 17.5 8 19.5 8 C22.5 8 23.5 11.5 21.5 13.5 Z" fill="#ffffff"/></svg>
    </div>
    <div class="nav-icon nav-messages" aria-label="Messages">
      <svg viewBox="0 0 30 30"><path d="M15 1 C23 1 29 6.5 29 13.5 C29 20.5 23 26 15 26 L9 29 L10 24 C4.5 22 1 18 1 13.5 C1 6.5 7 1 15 1 Z" fill="var(--icon-grey)"/><circle cx="9" cy="13.5" r="2" fill="#fff"/><circle cx="15" cy="13.5" r="2" fill="#fff"/><circle cx="21" cy="13.5" r="2" fill="#fff"/></svg>
    </div>
  </header>

  <section class="featured-card">
    <div class="featured-header">
      <span class="featured-name">LORA</span>
      <span class="featured-age">25</span>
      <span class="featured-job">Developer</span>
      <span class="distance">
        <svg viewBox="0 0 10 14"><path d="M5 0 C7.8 0 10 2.2 10 5 C10 8.5 5 14 5 14 C5 14 0 8.5 0 5 C0 2.2 2.2 0 5 0 Z" fill="var(--icon-grey)"/><circle cx="5" cy="5" r="2" fill="#fff"/></svg>
        8 miles
      </span>
    </div>
    <div class="featured-photo" role="img" aria-label="Profile photo of Lora">
      <div class="photo-dots">
        <span class="photo-dot is-active"></span>
        <span class="photo-dot"></span>
        <span class="photo-dot"></span>
        <span class="photo-dot"></span>
        <span class="photo-dot"></span>
      </div>
    </div>
    <div class="featured-actions">
      <div class="action-pass" aria-label="Pass">
        <svg viewBox="0 0 32 32"><circle cx="16" cy="16" r="15" fill="#fff" stroke="var(--pass-red)" stroke-width="1.6"/><path d="M10 10 L22 22 M22 10 L10 22" stroke="var(--pass-red)" stroke-width="1.6" stroke-linecap="round"/></svg>
      </div>
      <div class="see-more">SEE MORE</div>
      <div class="action-like" aria-label="Like">
        <svg viewBox="0 0 32 32"><circle cx="16" cy="16" r="16" fill="var(--like-green)"/><path d="M16 24 L9 17 C7 15 8 11 11.5 11 C13.5 11 15 12.5 16 14 C17 12.5 18.5 11 20.5 11 C24 11 25 15 23 17 Z" fill="#fff"/></svg>
      </div>
    </div>
  </section>

  <article class="profile-row row-one">
    <div class="row-photo" role="img" aria-label="Profile photo of Sam"></div>
    <div class="row-name">SAM</div>
    <div class="row-age">27</div>
    <div class="row-job">Developer</div>
    <div class="distance row-distance">
      <svg viewBox="0 0 10 14"><path d="M5 0 C7.8 0 10 2.2 10 5 C10 8.5 5 14 5 14 C5 14 0 8.5 0 5 C0 2.2 2.2 0 5 0 Z" fill="var(--icon-grey)"/><circle cx="5" cy="5" r="2" fill="var(--list-bg)"/></svg>
      8 miles
    </div>
    <div class="row-actions">
      <div class="mini-pass" aria-label="Pass"><svg viewBox="0 0 32 32"><circle cx="16" cy="16" r="15" fill="#fff" stroke="var(--pass-red)" stroke-width="1.6"/><path d="M10 10 L22 22 M22 10 L10 22" stroke="var(--pass-red)" stroke-width="1.6" stroke-linecap="round"/></svg></div>
      <div class="mini-like" aria-label="Like"><svg viewBox="0 0 32 32"><circle cx="16" cy="16" r="16" fill="var(--like-green)"/><path d="M16 24 L9 17 C7 15 8 11 11.5 11 C13.5 11 15 12.5 16 14 C17 12.5 18.5 11 20.5 11 C24 11 25 15 23 17 Z" fill="#fff"/></svg></div>
    </div>
  </article>

  <article class="profile-row row-two">
    <div class="row-photo" role="img" aria-label="Profile photo of Paula"></div>
    <div class="row-name">PAULA</div>
    <div class="row-age">22</div>
    <div class="row-job">Developer</div>
    <div class="distance row-distance">
      <svg viewBox="0 0 10 14"><path d="M5 0 C7.8 0 10 2.2 10 5 C10 8.5 5 14 5 14 C5 14 0 8.5 0 5 C0 2.2 2.2 0 5 0 Z" fill="var(--icon-grey)"/><circle cx="5" cy="5" r="2" fill="var(--list-bg)"/></svg>
      9 miles
    </div>
    <div class="row-actions">
      <div class="mini-pass" aria-label="Pass"><svg viewBox="0 0 32 32"><circle cx="16" cy="16" r="15" fill="#fff" stroke="var(--pass-red)" stroke-width="1.6"/><path d="M10 10 L22 22 M22 10 L10 22" stroke="var(--pass-red)" stroke-width="1.6" stroke-linecap="round"/></svg></div>
      <div class="mini-like" aria-label="Like"><svg viewBox="0 0 32 32"><circle cx="16" cy="16" r="16" fill="var(--like-green)"/><path d="M16 24 L9 17 C7 15 8 11 11.5 11 C13.5 11 15 12.5 16 14 C17 12.5 18.5 11 20.5 11 C24 11 25 15 23 17 Z" fill="#fff"/></svg></div>
    </div>
  </article>

</div>
</body>
</html>
```